Geschäftspapiere für familiengeführtes Zeitarbeitsunternehmen
Zielgruppe
Wir sind ein familiengeführtes Zeitarbeitsunternehmen. Somit haben wir 2 Zielgruppen, unsere Kunden und unsere Mitarbeiter. Eine Übersicht von uns findet man am besten auf unserer Website www.brandt-kraefte.de
Aufgabenstellung
Wir möchten 'nur' angepasstes Briefpapier mit neuen Daten. Gerne können Sie uns auch Vorschläge bezüglich eines verbesserten Designs machen.
Folgende Änderungen sind zu verarbeiten:
- die Geschäftstellen in Neustadt und Zell wurde geschlossen, daher ist Oberhof nun Hauptgeschäftsstelle
- die Firmierung hat sich geändert: das pw wurde entfernt
- Plaudernetz und bildoria kann raus
- Neu: UID DE 31 47 26 804
- Neu: Amtgericht Jena HRB 742391
- Neu rein bitte noch: Hinweis zum Datenschutz: https://brandt-kraefte.de/datenschutz/

```html
<!DOCTYPE html>
<html lang="de">
<head>
<meta charset="utf-8">
<title>Brandt Kräfte GmbH – Briefpapier</title>
<link href="https://fonts.googleapis.com/css2?family=Roboto:wght@300;400;700&display=swap" rel="stylesheet">
<style>
  :root {
    --brand-blue: #0284ae;
    --tint-blue: #e4f1f7;
    --text-grey: #6f6f6f;
    --paper: #ffffff;
  }
  html, body {
    margin: 0;
    padding: 0;
    overflow: hidden;
    background: var(--paper);
  }
  .letterhead {
    position: relative;
    width: 848px;
    height: 1200px;
    overflow: hidden;
    background: var(--paper);
    font-family: 'Roboto', sans-serif;
    font-weight: 300;
    color: var(--text-grey);
  }
  .backdrop-name {
    position: absolute;
    left: 0;
    top: 0;
    width: 848px;
    height: 210px;
  }
  .return-address {
    position: absolute;
    left: 81px;
    top: 196px;
    font-size: 11.5px;
    white-space: nowrap;
  }
  .brand-name {
    position: absolute;
    left: 590px;
    top: 180px;
    display: flex;
    align-items: center;
    gap: 8px;
    padding: 6px 8px;
    background: var(--paper);
    color: var(--brand-blue);
    font-size: 22px;
    font-weight: 700;
    line-height: 1;
    white-space: nowrap;
  }
  .brand-name__mark {
    width: 16px;
    height: 16px;
    background: var(--brand-blue);
  }
  .sender-block,
  .company-register {
    position: absolute;
    left: 648px;
    margin: 0;
    padding: 0;
    list-style: none;
    font-size: 13px;
    line-height: 24.2px;
    white-space: nowrap;
  }
  .sender-block { top: 262px; }
  .company-register { top: 1031px; }
  .privacy-note {
    position: absolute;
    left: 81px;
    top: 1133px;
    font-size: 11.5px;
    white-space: nowrap;
  }
  .footer-band {
    position: absolute;
    left: 0;
    bottom: 0;
    width: 848px;
    height: 41px;
    background: var(--brand-blue);
  }
  .footer-band__url {
    position: absolute;
    left: 648px;
    top: 11px;
    font-size: 15px;
    font-weight: 700;
    color: var(--paper);
    white-space: nowrap;
  }
</style>
</head>
<body>
<main class="letterhead">
  <svg class="backdrop-name" viewBox="0 0 848 210" aria-hidden="true">
    <text x="0" y="206" textLength="848" lengthAdjust="spacingAndGlyphs"
          font-family="Roboto, sans-serif" font-weight="700" font-size="270"
          fill="var(--tint-blue)">BRANDT</text>
  </svg>

  <div class="return-address">Brandt Kräfte GmbH · Birkenallee 12 · D-98559 Oberhof</div>

  <div class="brand-name">
    <span class="brand-name__mark"></span>
    <span>Brandt Kräfte</span>
  </div>

  <ul class="sender-block">
    <li>Brandt Kräfte GmbH</li>
    <li>Birkenallee 12</li>
    <li>D-98559 Oberhof</li>
    <li>Tel: +49 36842 471 230</li>
    <li>Fax: +49 36842 471 235</li>
    <li>kontakt@brandt-kraefte.de</li>
  </ul>

  <ul class="company-register">
    <li>Geschäftsführer:</li>
    <li>Marlo Brandt</li>
    <li>UID: DE 31 47 26 804</li>
    <li>Amtsgericht Jena</li>
    <li>HRB 742391</li>
  </ul>

  <div class="privacy-note">Hinweis zum Datenschutz: https://brandt-kraefte.de/datenschutz/</div>

  <footer class="footer-band">
    <span class="footer-band__url">www.brandt-kraefte.de</span>
  </footer>
</main>
</body>
</html>
```